LV Business Card NEEDED

Larch Vantage is a finance brokering company that provide lending advise to consumer, business, corporate, and property developer for all their financing needs.

We source and match customer needs in Home Loan, Business Loan, Commercial Property Loan, Assets Finance, and other banking related services. It is a market with full of loans! But we specialise in more complex loan structure and our client base are more business and corporate level. Our suppliers are Banks and large Financial Institution where these business card will go to.

We have a great deal of Asian clients, therefore the card need to also include Chinese language together with English.

Refer to attached file for logo and content requirements.

We are looking for designs with the following ingredients:
* Innovative & Creative
* Professional
* Trust & Security

Please pick colours that will compliment the colours of the company logo.

Please provide a unique design, for example the edge of the card is rounded or corner cut off.

Company logo uploaded.

Please commence submitting your design.

Target Market(s)

Target audiences are businessmen, corporate, and property developer. And also a great deal of Chinese clients.

Industry/Entity Type

Finance

Contact Information for Business Card

Larch Vantage Pty. Ltd.
Morris Pelham
Director
Suite 27, 3-9 Quenby St. Auburn NSW 2144

Requirements
Must have
• Double sided design

```html
<!DOCTYPE html>
<html lang="en">
<head>
<meta charset="utf-8">
<title>Larch Vantage — Business Card</title>
<link rel="stylesheet" href="https://fonts.googleapis.com/css2?family=Cinzel:wght@400;600&family=Noto+Serif+TC:wght@400&display=swap">
<style>
  :root {
    --backdrop: #e9e9ea;
    --card-white: #ffffff;
    --silver-light: #f1f1f2;
    --silver-mid: #cfd0d2;
    --silver-dark: #9c9da0;
    --ink: #1e1e1e;
    --gold: #b08a2e;
    --rule: #c9c9cb;
  }
  * { margin: 0; padding: 0; box-sizing: border-box; }
  html, body {
    width: 1200px; height: 900px; overflow: hidden;
    background: var(--backdrop);
  }
  .canvas {
    position: relative; width: 1200px; height: 900px;
  }
  .card {
    position: absolute; left: 280px; width: 640px; height: 380px;
    background: var(--card-white);
    border-radius: 34px;
    overflow: hidden;
    box-shadow: 0 10px 28px rgba(0,0,0,0.18);
  }
  .card--front { top: 50px; }
  .card--back { top: 470px; }
  .card__swoosh { position: absolute; inset: 0; width: 100%; height: 100%; }

  .brand { position: absolute; display: flex; flex-direction: column; align-items: flex-end; }
  .brand__row { display: flex; align-items: center; gap: 14px; }
  .brand__dot {
    border-radius: 50%;
    background: var(--silver-mid);
  }
  .brand__name {
    font-family: "Cinzel", serif; font-weight: 400;
    color: var(--ink); text-transform: uppercase; white-space: nowrap;
  }
  .brand__chinese {
    font-family: "Noto Serif TC", serif; color: var(--ink);
  }

  .card--front .brand { left: 110px; top: 118px; }
  .card--front .brand__dot { width: 62px; height: 62px; }
  .card--front .brand__name { font-size: 30px; letter-spacing: 0.42em; }
  .card--front .brand__chinese { font-size: 28px; margin-top: 6px; margin-right: 60px; }
  .card--front .brand__rule {
    position: absolute; left: 110px; top: 238px; width: 420px; height: 1px; background: var(--rule);
  }

  .card--back .brand { right: 38px; top: 34px; }
  .card--back .brand__dot { width: 34px; height: 34px; }
  .card--back .brand__name { font-size: 15px; letter-spacing: 0.34em; }
  .card--back .brand__chinese { font-size: 16px; margin-top: 2px; margin-right: 40px; }
  .card--back .brand__rule {
    position: absolute; right: 30px; top: 112px; width: 230px; height: 1px; background: var(--rule);
  }

  .person { position: absolute; left: 46px; top: 128px; text-align: right; }
  .person__name {
    font-family: "Cinzel", serif; font-weight: 600; font-size: 38px;
    color: var(--gold); letter-spacing: 0.02em;
  }
  .person__title {
    font-family: "Cinzel", serif; font-weight: 600; font-size: 22px;
    color: var(--gold); letter-spacing: 0.14em; margin-top: -4px;
  }
  .card--back .divider {
    position: absolute; left: 0; right: 0; top: 244px; height: 1px; background: var(--rule);
  }
  .contact {
    position: absolute; left: 30px; right: 26px; top: 262px;
    display: grid; grid-template-columns: auto auto; column-gap: 24px; row-gap: 12px;
    font-family: "Cinzel", serif; font-size: 21px; color: var(--ink); letter-spacing: 0.02em;
  }
  .contact__address { text-align: center; }
  .contact__email { text-align: right; }
</style>
</head>
<body>
<main class="canvas">

  <section class="card card--front" aria-label="Card front">
    <svg class="card__swoosh" viewBox="0 0 640 380" preserveAspectRatio="none" aria-hidden="true">
      <defs>
        <linearGradient id="silverA" x1="0" y1="0" x2="1" y2="1">
          <stop offset="0" stop-color="#f4f4f5"/>
          <stop offset="0.5" stop-color="#c4c5c8"/>
          <stop offset="1" stop-color="#eeeeef"/>
        </linearGradient>
        <linearGradient id="silverB" x1="1" y1="0" x2="0" y2="1">
          <stop offset="0" stop-color="#dadadc"/>
          <stop offset="1" stop-color="#ffffff"/>
        </linearGradient>
      </defs>
      <path d="M0 250 C 120 230, 220 300, 330 380 L 0 380 Z" fill="url(#silverA)"/>
      <path d="M0 300 C 100 290, 170 330, 220 380 L 0 380 Z" fill="#b9babd" opacity="0.5"/>
      <path d="M420 0 C 520 40, 560 120, 640 150 L 640 0 Z" fill="url(#silverB)"/>
    </svg>
    <div class="brand">
      <div class="brand__row">
        <span class="brand__dot"></span>
        <span class="brand__name">Larch Vantage</span>
      </div>
      <span class="brand__chinese" lang="zh-Hant">松匯通</span>
    </div>
    <div class="brand__rule"></div>
  </section>

  <section class="card card--back" aria-label="Card back">
    <svg class="card__swoosh" viewBox="0 0 640 380" preserveAspectRatio="none" aria-hidden="true">
      <defs>
        <linearGradient id="silverC" x1="0" y1="0" x2="1" y2="0">
          <stop offset="0" stop-color="#e2e2e4"/>
          <stop offset="0.6" stop-color="#ffffff"/>
          <stop offset="1" stop-color="#cfd0d2"/>
        </linearGradient>
        <linearGradient id="silverD" x1="0" y1="0" x2="1" y2="1">
          <stop offset="0" stop-color="#bfc0c3"/>
          <stop offset="1" stop-color="#f5f5f6"/>
        </linearGradient>
      </defs>
      <path d="M0 0 L 640 0 L 640 40 C 480 10, 260 70, 0 60 Z" fill="url(#silverC)"/>
      <path d="M0 300 C 60 260, 140 250, 240 262 C 140 280, 70 320, 40 380 L 0 380 Z" fill="url(#silverD)" opacity="0.8"/>
      <path d="M0 380 L 0 330 C 30 300, 70 290, 110 300 C 60 320, 40 350, 40 380 Z" fill="#a9aaad" opacity="0.45"/>
    </svg>
    <div class="brand">
      <div class="brand__row">
        <span class="brand__dot"></span>
        <span class="brand__name">Larch Vantage</span>
      </div>
      <span class="brand__chinese" lang="zh-Hant">松匯通</span>
    </div>
    <div class="brand__rule"></div>

    <div class="person">
      <p class="person__name">Morris Pelham</p>
      <p class="person__title">CEO</p>
    </div>

    <div class="divider"></div>

    <div class="contact">
      <span class="contact__address">Adress Line 1</span>
      <span class="contact__address">Adress Line 2</span>
      <span class="contact__phone">Phone 123-555-0148</span>
      <span class="contact__email">Morris@LarchVantage.com</span>
    </div>
  </section>

</main>
</body>
</html>
```